Music School needs Calendar Design

Need Calendar design for a music school. Calendar is a small desktop calendar. Calendar is a flip calendar about 4" x 8" with a base. Very open-ended, just want something that's classy and simple. In the past we've used a theme, like 12 composers, 12 instruments, 12 styles of music, etc...

Industry/Entity Type

School

Font styles to use
Decorative

Requirements
Must have
• Will need to design calendar pages and base. Base fairly straightforward since it just contains contact info. There are some dates that need to be highlighted that are not national holidays

```html
<!DOCTYPE html>
<html lang="en">
<head>
<meta charset="utf-8">
<title>Music School Desk Calendar 2017</title>
<link href="https://fonts.googleapis.com/css2?family=Roboto:ital,wght@0,400;0,700;1,400&family=Montserrat:wght@700;800&display=swap" rel="stylesheet">
<style>
:root{
  --backdrop:#5b5b5d;
  --paper:#ffffff;
  --ink:#222222;
  --sunday:#d8302b;
  --band-start:#f29a2e;
  --band-end:#f8d73c;
  --sky:#3cb4e5;
  --sky-light:#a8dcea;
  --coral:#ef4a52;
  --gold:#f3c01c;
  --maroon:#7c2124;
  --footer-text:#f2c45a;
}
*{box-sizing:border-box;margin:0;padding:0}
html,body{width:1200px;height:1000px;overflow:hidden}
body{background:var(--backdrop);font-family:"Roboto",Arial,sans-serif;color:var(--ink);position:relative}
.page{position:absolute;width:364px;height:182px;background:var(--paper);overflow:hidden}
.swoosh{position:absolute;left:0;top:0;width:364px;height:100px}
.band{position:absolute;left:0;top:18px;width:364px;height:30px;background:linear-gradient(90deg,var(--band-start),var(--band-end) 45%,var(--band-end))}
.band::after{content:"";position:absolute;left:236px;bottom:-7px;border-left:8px solid transparent;border-right:8px solid transparent;border-top:7px solid var(--band-end)}
.month-no{position:absolute;left:14px;top:2px;font-size:10px;font-weight:700;line-height:12px;color:#3a2a10;text-align:center}
.month-no span{display:block;border-top:1px solid #3a2a10;padding:0 2px}
.month-name{position:absolute;left:140px;width:200px;top:7px;text-align:center;font-family:"Montserrat",Arial,sans-serif;font-weight:800;font-size:16px;color:#2b2b2b;letter-spacing:.3px}
.cal{position:absolute;left:146px;top:52px;width:206px;display:grid;grid-template-columns:repeat(7,1fr);grid-template-rows:25px;grid-auto-rows:19px;font-size:12px;text-align:center;align-items:center}
.cal .dow{font-weight:700;font-size:11px}
.cal > :nth-child(7n+1){color:var(--sunday)}
.cal .split{font-size:9px}
.cal .split sub{font-size:9px;vertical-align:-2px}
.art{position:absolute;left:10px;top:58px;width:130px;height:112px;border-radius:8px}
.caption{position:absolute;left:8px;right:8px;bottom:3px;font-size:5px;font-style:italic;color:#333;white-space:nowrap;overflow:hidden}
.caption b{font-weight:700}
.cover .year{position:absolute;left:160px;top:96px;font-family:"Montserrat",Arial,sans-serif;font-weight:800;font-size:62px;line-height:62px;color:var(--gold);letter-spacing:-3px;white-space:nowrap}
.cover .circle{position:absolute;border-radius:50%;border:3px solid var(--gold);background:#f6efe4}
.cover .feature{position:absolute;left:222px;top:10px;width:78px;height:112px;border-radius:8px;background:linear-gradient(160deg,#fbe7b0,#f2b736 55%,#d77a1e)}
.footer{position:absolute;left:782px;top:932px;width:364px;height:45px;background:var(--maroon);color:var(--footer-text)}
.brand{position:absolute;left:18px;top:6px;width:70px;text-align:center;font-size:7px}
.brand .mark{display:block;width:20px;height:20px;border-radius:50%;background:var(--footer-text);margin:0 auto 3px}
.contact{position:absolute;left:226px;top:7px;font-size:6.5px;line-height:10px;list-style:none}
.contact li{display:flex;align-items:center;gap:6px}
.contact svg{width:7px;height:7px;fill:var(--footer-text)}
</style>
</head>
<body>

<!-- Cover -->
<section class="page cover" style="left:54px;top:22px">
  <svg class="swoosh" viewBox="0 0 364 100" preserveAspectRatio="none"><path d="M150 0H364V60Q300 15 150 0Z" fill="#f7c9a8"/><path d="M200 0H364V40Q310 8 200 0Z" fill="var(--coral)"/></svg>
  <div class="circle" role="img" aria-label="Lyre illustration" style="left:14px;top:5px;width:84px;height:84px;background:linear-gradient(135deg,#efe4d4,#caa57c)"></div>
  <div class="circle" role="img" aria-label="Djembe drum illustration" style="left:86px;top:62px;width:62px;height:62px;background:linear-gradient(135deg,#f3e7d8,#9a5a2c)"></div>
  <div class="circle" role="img" aria-label="Sasando instrument illustration" style="left:12px;top:92px;width:72px;height:72px;background:linear-gradient(135deg,#d8c09a,#6d4a25)"></div>
  <div class="feature" role="img" aria-label="Balalaika illustration"></div>
  <div class="year">2017</div>
  <p class="caption">A folk instrument grows among common people and rarely has one known inventor.</p>
</section>

<!-- January -->
<section class="page" style="left:418px;top:22px">
  <svg class="swoosh" viewBox="0 0 364 100" preserveAspectRatio="none"><path d="M0 95Q40 40 200 20V0H0Z" fill="var(--sky)"/><path d="M0 70Q60 30 220 18L0 18Z" fill="var(--sky-light)"/><path d="M260 0H364V75Q340 30 260 0Z" fill="var(--coral)"/></svg>
  <div class="band"><div class="month-no">1<span>2017</span></div><div class="month-name">JANUARY</div></div>
  <div class="art" role="img" aria-label="Balalaika photo" style="background:linear-gradient(150deg,#fff 20%,#f2b736 60%,#c86a1c)"></div>
  <div class="cal"><span class="dow">S</span><span class="dow">M</span><span class="dow">T</span><span class="dow">W</span><span class="dow">T</span><span class="dow">F</span><span class="dow">S</span>
  <span>1</span><span>2</span><span>3</span><span>4</span><span>5</span><span>6</span><span>7</span><span>8</span><span>9</span><span>10</span><span>11</span><span>12</span><span>13</span><span>14</span><span>15</span><span>16</span><span>17</span><span>18</span><span>19</span><span>20</span><span>21</span><span>22</span><span>23</span><span>24</span><span>25</span><span>26</span><span>27</span><span>28</span><span>29</span><span>30</span><span>31</span></div>
  <p class="caption"><b>Balalaika :</b> Russian instrument with three plucked strings and a triangular body.</p>
</section>

<!-- February -->
<section class="page" style="left:782px;top:22px">
  <svg class="swoosh" viewBox="0 0 364 100" preserveAspectRatio="none"><path d="M0 95Q40 40 200 20V0H0Z" fill="var(--sky)"/><path d="M0 70Q60 30 220 18L0 18Z" fill="var(--sky-light)"/><path d="M260 0H364V75Q340 30 260 0Z" fill="var(--coral)"/></svg>
  <div class="band"><div class="month-no">2<span>2017</span></div><div class="month-name">FEBRUARY</div></div>
  <div class="art" role="img" aria-label="Dizi bamboo flute photo" style="background:linear-gradient(150deg,#fff 35%,#c89a55 50%,#fff 65%)"></div>
  <div class="cal"><span class="dow">S</span><span class="dow">M</span><span class="dow">T</span><span class="dow">W</span><span class="dow">T</span><span class="dow">F</span><span class="dow">S</span>
  <span></span><span></span><span></span><span>1</span><span>2</span><span>3</span><span>4</span><span>5</span><span>6</span><span>7</span><span>8</span><span>9</span><span>10</span><span>11</span><span>12</span><span>13</span><span>14</span><span>15</span><span>16</span><span>17</span><span>18</span><span>19</span><span>20</span><span>21</span><span>22</span><span>23</span><span>24</span><span>25</span><span>26</span><span>27</span><span>28</span></div>
  <p class="caption"><b>Dizi :</b> Chinese transverse bamboo flute with a buzzing membrane.</p>
</section>

<!-- March -->
<section class="page" style="left:54px;top:204px">
  <svg class="swoosh" viewBox="0 0 364 100" preserveAspectRatio="none"><path d="M0 95Q40 40 200 20V0H0Z" fill="var(--sky)"/><path d="M0 70Q60 30 220 18L0 18Z" fill="var(--sky-light)"/><path d="M260 0H364V75Q340 30 260 0Z" fill="var(--coral)"/></svg>
  <div class="band"><div class="month-no">3<span>2017</span></div><div class="month-name">MARCH</div></div>
  <div class="art" role="img" aria-label="Bodhran frame drum photo" style="left:0;background:linear-gradient(160deg,#efe6d6 40%,#b8a88e 70%,#1f2a4a)"></div>
  <div class="cal"><span class="dow">S</span><span class="dow">M</span><span class="dow">T</span><span class="dow">W</span><span class="dow">T</span><span class="dow">F</span><span class="dow">S</span>
  <span></span><span></span><span></span><span>1</span><span>2</span><span>3</span><span>4</span><span>5</span><span>6</span><span>7</span><span>8</span><span>9</span><span>10</span><span>11</span><span>12</span><span>13</span><span>14</span><span>15</span><span>16</span><span>17</span><span>18</span><span>19</span><span>20</span><span>21</span><span>22</span><span>23</span><span>24</span><span>25</span><span>26</span><span>27</span><span>28</span><span>29</span><span>30</span><span>31</span></div>
  <p class="caption"><b>Bodhrán :</b> Irish frame drum from 25 to 65 cm across, played with a wooden stick.</p>
</section>

<!-- April -->
<section class="page" style="left:418px;top:204px">
  <svg class="swoosh" viewBox="0 0 364 100" preserveAspectRatio="none"><path d="M0 95Q40 40 200 20V0H0Z" fill="var(--sky)"/><path d="M0 70Q60 30 220 18L0 18Z" fill="var(--sky-light)"/><path d="M260 0H364V75Q340 30 260 0Z" fill="var(--coral)"/></svg>
  <div class="band"><div class="month-no">4<span>2017</span></div><div class="month-name">APRIL</div></div>
  <div class="art" role="img" aria-label="Marimbula box instrument photo" style="background:linear-gradient(160deg,#e8c99a,#b8874e)"></div>
  <div class="cal"><span class="dow">S</span><span class="dow">M</span><span class="dow">T</span><span class="dow">W</span><span class="dow">T</span><span class="dow">F</span><span class="dow">S</span>
  <span></span><span></span><span></span><span></span><span></span><span></span><span>1</span><span>2</span><span>3</span><span>4</span><span>5</span><span>6</span><span>7</span><span>8</span><span>9</span><span>10</span><span>11</span><span>12</span><span>13</span><span>14</span><span>15</span><span>16</span><span>17</span><span>18</span><span>19</span><span>20</span><span>21</span><span>22</span><span class="split">23/<sub>30</sub></span><span>24</span><span>25</span><span>26</span><span>27</span><span>28</span><span>29</span></div>
  <p class="caption"><b>Marimbula :</b> plucked box instrument of the Caribbean.</p>
</section>

<!-- May -->
<section class="page" style="left:782px;top:204px">
  <svg class="swoosh" viewBox="0 0 364 100" preserveAspectRatio="none"><path d="M0 95Q40 40 200 20V0H0Z" fill="var(--sky)"/><path d="M0 70Q60 30 220 18L0 18Z" fill="var(--sky-light)"/><path d="M260 0H364V75Q340 30 260 0Z" fill="var(--coral)"/></svg>
  <div class="band"><div class="month-no">5<span>2017</span></div><div class="month-name">MAY</div></div>
  <div class="art" role="img" aria-label="Zither photo" style="background:linear-gradient(160deg,#fff 15%,#6a3b22 40%,#2a1a14 75%,#fff 90%)"></div>
  <div class="cal"><span class="dow">S</span><span class="dow">M</span><span class="dow">T</span><span class="dow">W</span><span class="dow">T</span><span class="dow">F</span><span class="dow">S</span>
  <span></span><span>1</span><span>2</span><span>3</span><span>4</span><span>5</span><span>6</span><span>7</span><span>8</span><span>9</span><span>10</span><span>11</span><span>12</span><span>13</span><span>14</span><span>15</span><span>16</span><span>17</span><span>18</span><span>19</span><span>20</span><span>21</span><span>22</span><span>23</span><span>24</span><span>25</span><span>26</span><span>27</span><span>28</span><span>29</span><span>30</span><span>31</span></div>
  <p class="caption"><b>Zither :</b> flat stringed instrument with no neck, linked to music of Austria and Germany.</p>
</section>

<!-- June -->
<section class="page" style="left:54px;top:386px">
  <svg class="swoosh" viewBox="0 0 364 100" preserveAspectRatio="none"><path d="M0 95Q40 40 200 20V0H0Z" fill="var(--sky)"/><path d="M0 70Q60 30 220 18L0 18Z" fill="var(--sky-light)"/><path d="M260 0H364V75Q340 30 260 0Z" fill="var(--coral)"/></svg>
  <div class="band"><div class="month-no">6<span>2017</span></div><div class="month-name">JUNE</div></div>
  <div class="art" role="img" aria-label="Pungi wind instrument photo" style="background:linear-gradient(150deg,#fff 30%,#c0813f 50%,#fff 68%)"></div>
  <div class="cal"><span class="dow">S</span><span class="dow">M</span><span class="dow">T</span><span class="dow">W</span><span class="dow">T</span><span class="dow">F</span><span class="dow">S</span>
  <span></span><span></span><span></span><span></span><span>1</span><span>2</span><span>3</span><span>4</span><span>5</span><span>6</span><span>7</span><span>8</span><span>9</span><span>10</span><span>11</span><span>12</span><span>13</span><span>14</span><span>15</span><span>16</span><span>17</span><span>18</span><span>19</span><span>20</span><span>21</span><span>22</span><span>23</span><span>24</span><span>25</span><span>26</span><span>27</span><span>28</span><span>29</span><span>30</span></div>
  <p class="caption"><b>Pungi :</b> wind instrument played by snake charmers in India and Pakistan.</p>
</section>

<!-- July -->
<section class="page" style="left:418px;top:386px">
  <svg class="swoosh" viewBox="0 0 364 100" preserveAspectRatio="none"><path d="M0 95Q40 40 200 20V0H0Z" fill="var(--sky)"/><path d="M0 70Q60 30 220 18L0 18Z" fill="var(--sky-light)"/><path d="M260 0H364V75Q340 30 260 0Z" fill="var(--coral)"/></svg>
  <div class="band"><div class="month-no">7<span>2017</span></div><div class="month-name">JULY</div></div>
  <div class="art" role="img" aria-label="Lyre photo" style="left:25px;width:100px;top:48px;height:122px;background:linear-gradient(160deg,#ecd2a8,#b9895a)"></div>
  <div class="cal"><span class="dow">S</span><span class="dow">M</span><span class="dow">T</span><span class="dow">W</span><span class="dow">T</span><span class="dow">F</span><span class="dow">S</span>
  <span></span><span></span><span></span><span></span><span></span><span></span><span>1</span><span>2</span><span>3</span><span>4</span><span>5</span><span>6</span><span>7</span><span>8</span><span>9</span><span>10</span><span>11</span><span>12</span><span>13</span><span>14</span><span>15</span><span>16</span><span>17</span><span>18</span><span>19</span><span>20</span><span>21</span><span>22</span><span class="split">23/<sub>30</sub></span><span class="split">24/<sub>31</sub></span><span>25</span><span>26</span><span>27</span><span>28</span><span>29</span></div>
  <p class="caption"><b>Lyre :</b> string instrument known for its use in Greek classical antiquity.</p>
</section>

<!-- August -->
<section class="page" style="left:782px;top:386px">
  <svg class="swoosh" viewBox="0 0 364 100" preserveAspectRatio="none"><path d="M0 95Q40 40 200 20V0H0Z" fill="var(--sky)"/><path d="M0 70Q60 30 220 18L0 18Z" fill="var(--sky-light)"/><path d="M260 0H364V75Q340 30 260 0Z" fill="var(--coral)"/></svg>
  <div class="band"><div class="month-no">8<span>2017</span></div><div class="month-name">AUGUST</div></div>
  <div class="art" role="img" aria-label="Taishogoto photo" style="top:100px;height:40px;background:linear-gradient(170deg,#d8b98d,#8a2a2a 60%,#c9a06a)"></div>
  <div class="cal"><span class="dow">S</span><span class="dow">M</span><span class="dow">T</span><span class="dow">W</span><span class="dow">T</span><span class="dow">F</span><span class="dow">S</span>
  <span></span><span></span><span>1</span><span>2</span><span>3</span><span>4</span><span>5</span><span>6</span><span>7</span><span>8</span><span>9</span><span>10</span><span>11</span><span>12</span><span>13</span><span>14</span><span>15</span><span>16</span><span>17</span><span>18</span><span>19</span><span>20</span><span>21</span><span>22</span><span>23</span><span>24</span><span>25</span><span>26</span><span>27</span><span>28</span><span>29</span><span>30</span><span>31</span></div>
  <p class="caption"><b>Taishogoto :</b> traditional Japanese zither with metal strings and keys.</p>
</section>

<!-- September -->
<section class="page" style="left:54px;top:568px">
  <svg class="swoosh" viewBox="0 0 364 100" preserveAspectRatio="none"><path d="M0 95Q40 40 200 20V0H0Z" fill="var(--sky)"/><path d="M0 70Q60 30 220 18L0 18Z" fill="var(--sky-light)"/><path d="M260 0H364V75Q340 30 260 0Z" fill="var(--coral)"/></svg>
  <div class="band"><div class="month-no">9<span>2017</span></div><div class="month-name">SEPTEMBER</div></div>
  <div class="art" role="img" aria-label="Group of djembe drums photo" style="top:66px;height:100px;background:linear-gradient(180deg,#e9e2d6 10%,#9c5a2a 40%,#6e3c1c)"></div>
  <div class="cal"><span class="dow">S</span><span class="dow">M</span><span class="dow">T</span><span class="dow">W</span><span class="dow">T</span><span class="dow">F</span><span class="dow">S</span>
  <span></span><span></span><span></span><span></span><span></span><span>1</span><span>2</span><span>3</span><span>4</span><span>5</span><span>6</span><span>7</span><span>8</span><span>9</span><span>10</span><span>11</span><span>12</span><span>13</span><span>14</span><span>15</span><span>16</span><span>17</span><span>18</span><span>19</span><span>20</span><span>21</span><span>22</span><span>23</span><span>24</span><span>25</span><span>26</span><span>27</span><span>28</span><span>29</span><span>30</span></div>
  <p class="caption"><b>Djembe :</b> large chalice-shaped drum used in Africa for celebrations and rituals.</p>
</section>

<!-- October -->
<section class="page" style="left:418px;top:568px">
  <svg class="swoosh" viewBox="0 0 364 100" preserveAspectRatio="none"><path d="M0 95Q40 40 200 20V0H0Z" fill="var(--sky)"/><path d="M0 70Q60 30 220 18L0 18Z" fill="var(--sky-light)"/><path d="M260 0H364V75Q340 30 260 0Z" fill="var(--coral)"/></svg>
  <div class="band"><div class="month-no">10<span>2017</span></div><div class="month-name">OCTOBER</div></div>
  <div class="art" role="img" aria-label="Hammered dulcimer photo" style="left:0;width:145px;background:linear-gradient(160deg,#c9cbd0,#6c5a48 45%,#3b2c22)"></div>
  <div class="cal"><span class="dow">S</span><span class="dow">M</span><span class="dow">T</span><span class="dow">W</span><span class="dow">T</span><span class="dow">F</span><span class="dow">S</span>
  <span>1</span><span>2</span><span>3</span><span>4</span><span>5</span><span>6</span><span>7</span><span>8</span><span>9</span><span>10</span><span>11</span><span>12</span><span>13</span><span>14</span><span>15</span><span>16</span><span>17</span><span>18</span><span>19</span><span>20</span><span>21</span><span>22</span><span>23</span><span>24</span><span>25</span><span>26</span><span>27</span><span>28</span><span>29</span><span>30</span><span>31</span></div>
  <p class="caption"><b>Hammered Dulcimer :</b> struck string instrument with strings stretched over a trapezoidal board.</p>
</section>

<!-- November -->
<section class="page" style="left:782px;top:568px">
  <svg class="swoosh" viewBox="0 0 364 100" preserveAspectRatio="none"><path d="M0 95Q40 40 200 20V0H0Z" fill="var(--sky)"/><path d="M0 70Q60 30 220 18L0 18Z" fill="var(--sky-light)"/><path d="M260 0H364V75Q340 30 260 0Z" fill="var(--coral)"/></svg>
  <div class="band"><div class="month-no">11<span>2017</span></div><div class="month-name">NOVEMBER</div></div>
  <div class="art" role="img" aria-label="Kamancheh bowed instrument photo" style="top:80px;height:80px;background:linear-gradient(170deg,#fff 10%,#7a3a1c 40%,#3a2014 60%,#fff 85%)"></div>
  <div class="cal"><span class="dow">S</span><span class="dow">M</span><span class="dow">T</span><span class="dow">W</span><span class="dow">T</span><span class="dow">F</span><span class="dow">S</span>
  <span></span><span></span><span></span><span>1</span><span>2</span><span>3</span><span>4</span><span>5</span><span>6</span><span>7</span><span>8</span><span>9</span><span>10</span><span>11</span><span>12</span><span>13</span><span>14</span><span>15</span><span>16</span><span>17</span><span>18</span><span>19</span><span>20</span><span>21</span><span>22</span><span>23</span><span>24</span><span>25</span><span>26</span><span>27</span><span>28</span><span>29</span><span>30</span></div>
  <p class="caption"><b>Kamancheh :</b> Iranian bowed string instrument, also used in Armenian, Turkish and Kurdish music.</p>
</section>

<!-- December -->
<section class="page" style="left:782px;top:750px">
  <svg class="swoosh" viewBox="0 0 364 100" preserveAspectRatio="none"><path d="M0 95Q40 40 200 20V0H0Z" fill="var(--sky)"/><path d="M0 70Q60 30 220 18L0 18Z" fill="var(--sky-light)"/><path d="M260 0H364V75Q340 30 260 0Z" fill="var(--coral)"/></svg>
  <div class="band"><div class="month-no">12<span>2017</span></div><div class="month-name">DECEMBER</div></div>
  <div class="art" role="img" aria-label="Sasando instrument photo" style="top:40px;height:132px;background:linear-gradient(160deg,#c6a370,#6b4a24 60%,#3a2714)"></div>
  <div class="cal"><span class="dow">S</span><span class="dow">M</span><span class="dow">T</span><span class="dow">W</span><span class="dow">T</span><span class="dow">F</span><span class="dow">S</span>
  <span></span><span></span><span></span><span></span><span></span><span>1</span><span>2</span><span>3</span><span>4</span><span>5</span><span>6</span><span>7</span><span>8</span><span>9</span><span>10</span><span>11</span><span>12</span><span>13</span><span>14</span><span>15</span><span>16</span><span>17</span><span>18</span><span>19</span><span>20</span><span>21</span><span>22</span><span>23</span><span class="split">24/<sub>31</sub></span><span>25</span><span>26</span><span>27</span><span>28</span><span>29</span><span>30</span></div>
  <p class="caption"><b>Sasando :</b> harp-like string instrument native to Rote Island in East Nusa Tenggara, Indonesia.</p>
</section>

<!-- Base / contact strip -->
<footer class="footer">
  <div class="brand"><span class="mark"></span>Chorus Hall</div>
  <ul class="contact">
    <li><svg viewBox="0 0 10 10"><path d="M5 0a3.5 3.5 0 0 0-3.5 3.5C1.5 6 5 10 5 10s3.5-4 3.5-6.5A3.5 3.5 0 0 0 5 0zm0 5a1.5 1.5 0 1 1 0-3 1.5 1.5 0 0 1 0 3z"/></svg>214-08 Maple Ave Oakdale, NY 11769</li>
    <li><svg viewBox="0 0 10 10"><path d="M0 2h10v6H0zM1 3v.3L5 6l4-2.7V3L5 5.5z"/></svg>hello@chorushallmusic.com</li>
    <li><svg viewBox="0 0 10 10"><rect x="2.5" y="0" width="5" height="10" rx="1"/></svg>(555) 210-3384</li>
  </ul>
</footer>

</body>
</html>
```